Business card Zottelgarten

Business card is for a self-employed dog trainer with own dog school. Name and logo of the dog school are available. Color specifications as well. The design should be classy and minimalist, but also modern. An already existing idea would be: Front: Only the logo Back: Contact data

Font styles to use
Serif
Sans Serif
Other font styles liked:
• Trajan Pro

Colors
f78f20

Requirements
Must have
• Name: Margit Wendler-Rasch Title: Dipl. Dog Trainer Contain my logo Follow my font and color preferences (see files)

```html
<!DOCTYPE html>
<html lang="de">
<head>
<meta charset="utf-8">
<title>Zottelgarten – Visitenkarte</title>
<link rel="stylesheet" href="https://fonts.googleapis.com/css2?family=Cinzel:wght@400&display=swap">
<style>
  :root {
    --brand-orange: #f78f20;
    --card-white: #ffffff;
    --mark-ink: #b4600c;
  }
  html, body {
    margin: 0;
    padding: 0;
    width: 1200px;
    height: 699px;
    overflow: hidden;
    background: var(--brand-orange);
  }
  .business-card {
    position: relative;
    width: 1200px;
    height: 699px;
    background: var(--brand-orange);
    font-family: "Cinzel", "Trajan Pro", serif;
    color: var(--card-white);
  }
  .brand-mark {
    position: absolute;
    left: 40px;
    top: 110px;
    width: 482px;
    height: 482px;
  }
  .brand-name {
    font-family: "Cinzel", "Trajan Pro", serif;
    font-size: 44px;
    fill: var(--mark-ink);
    letter-spacing: 1px;
  }
  .contact-details {
    position: absolute;
    left: 517px;
    top: 268px;
    margin: 0;
  }
  .contact-line {
    margin: 0;
    font-size: 38px;
    line-height: 1;
    letter-spacing: 1px;
    white-space: nowrap;
  }
  .contact-line + .contact-line {
    margin-top: 67px;
  }
</style>
</head>
<body>
  <main class="business-card">
    <svg class="brand-mark" viewBox="0 0 482 482" role="img" aria-label="Zottelgarten">
      <defs>
        <linearGradient id="mark-fade" x1="0" y1="0" x2="1" y2="0">
          <stop offset="0" stop-color="#ffffff"/>
          <stop offset="0.85" stop-color="#f78f20"/>
        </linearGradient>
      </defs>
      <circle cx="241" cy="241" r="236" fill="url(#mark-fade)" stroke="#ffffff" stroke-width="5"/>
      <text class="brand-name" x="241" y="256" text-anchor="middle">Zottelgarten</text>
    </svg>

    <section class="contact-details">
      <p class="contact-line">Name: Margit Wendler-Rasch</p>
      <p class="contact-line">Title: Dipl. Hundetrainerin</p>
    </section>
  </main>
</body>
</html>
```